Web Design Project

We are an IT System Integrator. We provide Norvik 500 ERP System, CRM etc. We also provide hardware, networking servicing. Please look at www.brinquot.com.sg. They provide the same service as us. We like to redesign our web site. I will attached the color that I prefer for reference.

Our website is www.ravdu.com.sg.  It has been created about 14 years ago.  We are trying to revamp it with a new look and information.   The new website must be informative, fast.    I have attached an attachment which show the color that I prefer(brownish golden).   

Our competitor (www.brinquot.com) is carrying the same trade as us.  They have all the informations In their website that we will like to have.  Therefore I recommend you to take a look at my competitor website and have a better   
understanding on the kind of information I would like to have for my new website.

This project is guarantee to the person with the best design.  We can have it guarantee.

Target Market(s)

Corporate and companies

Industry/Entity Type

Hardware

```html
<!DOCTYPE html>
<html lang="en">
<head>
<meta charset="utf-8">
<title>Ravdu Information System</title>
<link href="https://fonts.googleapis.com/css2?family=Roboto+Slab:wght@400;500&family=PT+Sans:wght@400;700&family=Roboto+Condensed:wght@400&family=Architects+Daughter&display=swap" rel="stylesheet">
<style>
:root{
  --brown:#7a552b;
  --brown-dark:#6a4822;
  --brown-light:#a57a43;
  --gold:#c99d4c;
  --nav-gold:#e7b061;
  --hero-bg:#cfd8d5;
  --grey-panel:#e3e3e3;
  --text:#2b2b2b;
  --white:#ffffff;
}
*{margin:0;padding:0;box-sizing:border-box}
html,body{width:1063px;height:1200px;overflow:hidden;background:var(--white)}
body{position:relative;font-family:"PT Sans",Arial,sans-serif;color:var(--text)}
.abs{position:absolute}

.site-header{left:0;top:0;width:1063px;height:80px;background:var(--white)}
.brand{left:118px;top:22px;display:flex;align-items:center;gap:10px}
.brand-mark{width:36px;height:36px;border-radius:50%;background:var(--gold)}
.brand-name{font-family:"Roboto Condensed",sans-serif;font-size:25px;color:var(--gold);font-weight:400}
.quote-btn{left:767px;top:26px;width:173px;height:30px;border-radius:3px;background:linear-gradient(#8d6536,#5f411d);color:var(--white);font-family:"PT Sans",sans-serif;font-size:17px;display:flex;align-items:center;justify-content:center}

.band{left:0;top:80px;width:1063px;height:339px;background:linear-gradient(180deg,#6e4c26 0%,#8a6333 40%,#a67c45 100%)}
.main-nav{left:0;top:96px;width:1063px;display:flex;justify-content:center;align-items:center;gap:18px;font-family:"Roboto Condensed",sans-serif;font-size:15px;color:var(--nav-gold);text-transform:uppercase}
.main-nav .current{color:var(--white)}
.nav-dot{width:7px;height:7px;background:#f2e2c8;border:1px solid #fff}

.hero{left:123px;top:134px;width:818px;height:336px}
.hero-title{left:166px;top:228px;font-family:"Roboto Slab",serif;font-weight:500;font-size:31px;line-height:27px;color:var(--brown)}
.hero-sub{left:166px;top:298px;font-family:"Roboto Slab",serif;font-size:20px;line-height:19px;color:#3c3c3c}
.hero-btn{left:167px;top:353px;width:84px;height:25px;border-radius:3px;background:linear-gradient(#fafafa,#dcdcdc);box-shadow:0 1px 2px rgba(0,0,0,.3);font-family:"Roboto Slab",serif;font-size:14px;color:#444;display:flex;align-items:center;justify-content:center}

h2.section-title{font-family:"Roboto Slab",serif;font-weight:500;color:var(--brown);font-size:20px}
.welcome-title{left:123px;top:538px}
.welcome-photo{left:123px;top:581px;width:145px;height:107px;background:linear-gradient(160deg,#bfe4f8,#3f8fc9 60%,#1b5d99)}
.body-text{font-size:12.3px;line-height:17px;color:#2e2e2e}
.welcome-p1{left:290px;top:575px;width:402px}
.welcome-p2{left:123px;top:707px;width:570px}

.stories-title{left:120px;top:786px}
.stories-text{left:121px;top:817px;width:250px}
.read-more{color:var(--brown);font-weight:700;font-size:12.5px}
.testi-title{left:421px;top:790px}
.testi-quote{left:421px;top:826px;width:240px;font-size:10.5px;line-height:14px}
.testi-author{left:421px;top:876px;font-size:11.5px;line-height:12px;color:#a0752f}
.testi-note{left:421px;top:903px;font-size:10.5px}

.partners{left:123px;top:965px;width:560px;height:60px;display:flex;align-items:center;justify-content:space-between;font-family:"PT Sans",sans-serif;color:#8c8c8c}
.partners span{font-size:22px}
.partner-badge{width:50px;height:50px;border-radius:50%;border:2px solid #a7a7a7}

.news{left:723px;top:527px;width:217px;height:299px;background:var(--grey-panel);border-radius:3px;padding:10px 15px}
.panel-title{font-family:"Roboto Slab",serif;font-weight:500;font-size:19px;color:#111;margin-bottom:14px}
.news-item{margin-bottom:11px;font-size:10.5px;line-height:13.8px}
.news-item h3{font-size:11px;font-weight:700;color:#a0752f;line-height:13.5px}
.news-item b{color:#111;font-weight:400}
.contact{left:723px;top:837px;width:217px;height:185px;background:var(--gold);border-radius:3px;padding:10px 15px;color:var(--white)}
.contact .panel-title{color:var(--white);margin-bottom:10px}
.contact h3{font-size:13px;font-weight:400;line-height:14px}
.contact p{font-size:10.5px;line-height:13.5px}
.contact .tel{margin-top:14px;font-size:11px}

.footer-strip{left:0;top:1085px;width:1063px;height:9px;background:#e4e1de}
.site-footer{left:0;top:1094px;width:1063px;height:106px;background:linear-gradient(180deg,#7a552b,#6a4822)}
.footer-nav{left:0;top:1130px;width:1063px;display:flex;justify-content:center;gap:15px;font-family:"Architects Daughter",sans-serif;font-size:9px;color:var(--white)}
.copyright{left:0;top:1154px;width:1063px;text-align:center;font-family:"Architects Daughter",sans-serif;font-size:9px;color:var(--white)}
</style>
</head>
<body>

<header class="site-header abs">
  <div class="brand abs"><span class="brand-mark"></span><span class="brand-name">Ravdu Information System</span></div>
  <div class="quote-btn abs">Request a quote</div>
</header>

<div class="band abs"></div>

<nav class="main-nav abs">
  <span class="current">Home</span><span class="nav-dot"></span>
  <span>Solution</span><span class="nav-dot"></span>
  <span>Hardware</span><span class="nav-dot"></span>
  <span>Services</span><span class="nav-dot"></span>
  <span>Clients</span><span class="nav-dot"></span>
  <span>About Us</span><span class="nav-dot"></span>
  <span>Contact Us</span>
</nav>

<svg class="hero abs" viewBox="0 0 818 336" width="818" height="336">
  <defs>
    <linearGradient id="heroPhoto" x1="0" x2="1" y1="0" y2="0">
      <stop offset="0" stop-color="#cfd8d5" stop-opacity="0"/>
      <stop offset="0.25" stop-color="#b9b6b0"/>
      <stop offset="0.6" stop-color="#d8b9a2"/>
      <stop offset="1" stop-color="#e9e9e6"/>
    </linearGradient>
    <clipPath id="heroClip">
      <path d="M0 6 Q0 0 6 0 H812 Q818 0 818 6 V310 Q600 332 409 336 Q200 332 2 310 Q0 309 0 304 Z"/>
    </clipPath>
  </defs>
  <g clip-path="url(#heroClip)">
    <rect width="818" height="336" fill="var(--hero-bg)"/>
    <rect x="330" y="0" width="488" height="336" fill="url(#heroPhoto)" role="img" aria-label="Photo of a smiling business team in office attire"/>
  </g>
</svg>
<h1 class="hero-title abs">Accounting software,<br>networking,</h1>
<p class="hero-sub abs">hardware maintenance and<br>consulting assistance</p>
<div class="hero-btn abs">Read More</div>

<h2 class="section-title welcome-title abs">Welcome to Ravdu Information System</h2>
<div class="welcome-photo abs" role="img" aria-label="Illustration of business people silhouettes in front of a globe"></div>
<p class="body-text welcome-p1 abs">Aenean dapibus lorem laoreet ante pharetra ornare malesuada orci ornare. Ut volutpat ipsum ipsum, eget suscipit mauris. Sed sed nisl ac justo rutrum convallis. Fusce facilisis, nunc et viverra iaculis, arcu augue tempor ipsum, ut auctor sapien justo ac metus. Morbi adipiscing sodales condimentum. Nunc porta hendrerit turpis, nec pharetra enim interdum id. Aenean dapibus lorem laoreet ante pharetra ornare malesuada orci ornare. Ut volutpat ipsum ipsum, eget suscipit mauris.</p>
<p class="body-text welcome-p2 abs">Aenean dapibus lorem laoreet ante pharetra ornare malesuada orci ornare. Ut volutpat ipsum ipsum, eget suscipit mauris. Sed sed nisl ac justo rutrum convallis. Fusce facilisis, nunc et viverra iaculis, arcu augue tempor ipsum, ut auctor sapien justo ac metus. Morbi adipiscing sodales condimentum.</p>

<h2 class="section-title stories-title abs">Success Stories</h2>
<p class="body-text stories-text abs">Sed lacinia vulputate dolor, nec congue nunc accumsan at. Praesent leo magna, imperdiet et mollis sed, hendrerit id nunc. Vestibulum et dolor enim. Cum sociis natoque penatibus et magnis dis<br><span class="read-more">Read More</span></p>

<h2 class="section-title testi-title abs">Testimonials</h2>
<p class="testi-quote abs">" The [staff at]...Ravdu Information Systems, are friendly attentive and supportive. Any problem, regardless of time, ... "</p>
<p class="testi-author abs">-Group Data &amp; System Manager,<br>Kestrel Technologies Ltd</p>
<p class="testi-note abs">(Article featured in Tech Asia Review magazine, Oct 2000)</p>

<div class="partners abs">
  <span>Norvik</span>
  <span>Norvik Acpro ERP</span>
  <span class="partner-badge"></span>
  <span>Halden</span>
  <span>Strata</span>
</div>

<aside class="news abs">
  <h2 class="panel-title">Recent News</h2>
  <div class="news-item"><h3>Nam quis ligula a nibh fermentum venenatis vitae</h3>Sed lacinia vulputate dolor, nec congue nunc accumsan at. Praesent leo magna... <b>read more</b></div>
  <div class="news-item"><h3>Aenean dapibus lorem laoreet ante pharetra ornare</h3>Ut volutpat ipsum ipsum, eget suscipit mauris. Sed sed nisl ac justo rutrum convallis... <b>read more</b></div>
  <div class="news-item"><h3>Aenean dapibus lorem laoreet ante pharetra ornare</h3>Ut volutpat ipsum ipsum, eget suscipit mauris. Sed sed nisl ac justo rutrum convallis... <b>read more</b></div>
</aside>

<aside class="contact abs">
  <h2 class="panel-title">Contact Us</h2>
  <h3>Ravdu Information<br>System Pte Ltd</h3>
  <p>18 Alder Lane<br># 03-21/22 Parkview Hub<br>Singapore - 559812</p>
  <p class="tel"><b>Telephone No:</b> (065) 6120 - 4410<br><b>Facsimile No:</b> (065) 6120 - 4417</p>
</aside>

<div class="footer-strip abs"></div>
<footer class="site-footer abs"></footer>
<nav class="footer-nav abs">
  <span>Home</span><span>Solution</span><span>Hardware</span><span>Services</span><span>Clients</span><span>About Us</span><span>Contact Us</span>
</nav>
<p class="copyright abs">© Copyright 2013. All Rights Reserved.</p>

</body>
</html>
```